Business Card Design

I need a business card for my rental business. The business is named:
Hire a Vorlatrike Brenmoor
www.hireavorlatrikebrenmoor.example
(555) 014-2937
This will be a business card that I will leave at other businesses as advertisement so it needs to have the name, website, and phone number.
Please feel free to be creative. This is a new business so I have no designs.
Thank you very much for your time and I look forward to receiving your designs
Target Market(s)
Local rental customers
Industry/Entity Type
Business
Contact Information for Business Card
Please check out my website:
Other font styles liked:
- anything creative
Colors
Designer to choose colors to be used in the design.
Requirements
Must have
- Business name, phone, website. Rentals available hourly or daily. Book online

```html
<!DOCTYPE html>
<html lang="en">
<head>
<meta charset="utf-8">
<title>Hire a Vorlatrike Brenmoor – Business Card</title>
<link rel="stylesheet" href="https://fonts.googleapis.com/css2?family=Bodoni+Moda:opsz,wght@6..96,700&family=Didact+Gothic&display=swap">
<style>
  :root {
    --card-dark: #333333;
    --facet-mid: #474747;
    --facet-light: #525252;
    --facet-right: #484848;
    --facet-shadow: #3a3a3a;
    --band-grey: #9a9a9a;
    --ink-white: #ffffff;
    --ink-black: #111111;
  }
  html, body {
    margin: 0;
    padding: 0;
    width: 1200px;
    height: 686px;
    overflow: hidden;
    background: var(--card-dark);
  }
  .business-card {
    display: block;
    width: 1200px;
    height: 686px;
  }
  .card-base { fill: var(--card-dark); }
  .facet-mid { fill: var(--facet-mid); }
  .facet-light { fill: var(--facet-light); }
  .facet-right { fill: var(--facet-right); }
  .facet-shadow { fill: var(--facet-shadow); }
  .booking-band { fill: var(--band-grey); }
  .display-label {
    font-family: "Bodoni Moda", "Didot", serif;
    font-weight: 700;
    fill: var(--ink-white);
  }
  .detail-text {
    font-family: "Didact Gothic", "Century Gothic", sans-serif;
    fill: var(--ink-white);
  }
  .business-name { letter-spacing: 1px; }
  .booking-label { fill: var(--ink-black); }
</style>
</head>
<body>
<svg class="business-card" viewBox="0 0 1200 686" xmlns="http://www.w3.org/2000/svg" aria-label="Hire a Vorlatrike Brenmoor business card">
  <g class="card-background">
    <rect class="card-base" x="0" y="0" width="1200" height="686"/>
    <polygon class="facet-mid" points="411,541 906,3 906,541"/>
    <polygon class="facet-light" points="705,541 906,320 906,541"/>
    <polygon class="facet-right" points="906,320 1200,6 1200,541"/>
    <polygon class="facet-shadow" points="906,320 1200,541 906,541"/>
    <rect class="booking-band" x="0" y="541" width="1200" height="145"/>
  </g>

  <g class="business-identity">
    <text class="detail-text business-name" x="168" y="165" font-size="36">Hire a Vorlatrike Brenmoor</text>
  </g>

  <g class="rental-offer">
    <text class="display-label" x="166" y="265" font-size="80" textLength="528" lengthAdjust="spacingAndGlyphs">RENTALS AVAILABLE</text>
    <text class="detail-text" x="722" y="251" font-size="44" textLength="299" lengthAdjust="spacingAndGlyphs">Hourly or Daily</text>
  </g>

  <g class="phone-contact">
    <text class="display-label" x="169" y="364" font-size="86" textLength="180" lengthAdjust="spacingAndGlyphs">PHONE</text>
    <text class="detail-text" x="375" y="349" font-size="44" textLength="307" lengthAdjust="spacingAndGlyphs">(555) 014-2937</text>
  </g>

  <g class="online-booking">
    <text class="detail-text" x="123" y="623" font-size="44" textLength="952" lengthAdjust="spacingAndGlyphs"><tspan class="booking-label">Book Online: </tspan>www.hireavorlatrikebrenmoor.example</text>
  </g>
</svg>
</body>
</html>
```